Awesome Web Design Project

must have a link to palsphere of the homepage preferably a scrolling view of our palsphere page!

We are an exciting new electrical company with a strong focus on energy efficiency and offering the latest technologies.

The design should allow easy navigation, there shouldn't be too many menus, It should look clean and sleek, Colours to consider could be green, silver/chrome, black,

The site should convey technology, efficiency and simplicity

Must be viewable on all devices, pc's, tablets, phones ie Responsive

Logo and some pics uploaded!

Industry/Entity Type

Electrical

Requirements
Must have
• must include the following pages,
about us
our services
gallery
contact us
Connect with us
Nice to have
• Would be great if the website design used a user friendly cms,
Should not have
• too many links, menus, clutter it should be clean and easy to navigate

```html
<!DOCTYPE html>
<html lang="en">
<head>
<meta charset="utf-8">
<title>Larkin Electrical – About Us</title>
<link href="https://fonts.googleapis.com/css2?family=Arimo:wght@400;700&display=swap" rel="stylesheet">
<style>
  :root {
    --page-bg: #eeefee;
    --lime: #c2c62e;
    --teal: #1d4a52;
    --ink: #0f3338;
    --panel: #f7f8f8;
    --white: #ffffff;
    --footer: #17444a;
  }
  * { box-sizing: border-box; margin: 0; padding: 0; }
  html, body { width: 1200px; height: 820px; overflow: hidden; }
  body {
    position: relative;
    background: var(--page-bg);
    font-family: "Arimo", Arial, sans-serif;
    color: var(--ink);
  }
  .brand {
    position: absolute; top: 14px; left: 0; width: 1200px;
    display: flex; justify-content: center; align-items: center; gap: 14px;
  }
  .brand-mark { width: 46px; height: 46px; background: var(--lime); }
  .brand-name {
    font-size: 44px; font-weight: 700; color: var(--teal);
    letter-spacing: 2px; line-height: 1;
  }
  .main-nav {
    position: absolute; top: 90px; left: 0; width: 1200px; height: 40px;
    background: var(--lime);
  }
  .main-nav a {
    position: absolute; top: 12px; font-size: 16px; color: var(--ink);
    text-decoration: none;
  }
  .main-nav a.active { color: var(--white); }
  .search {
    position: absolute; top: 5px; left: 839px; width: 203px; height: 30px;
    background: var(--white); border-radius: 9px;
  }
  .search svg.lens { position: absolute; left: 5px; top: 8px; }
  .search .divider {
    position: absolute; left: 24px; top: 5px; height: 20px;
    border-left: 1px dotted #9a9a9a;
  }
  .search .placeholder {
    position: absolute; left: 32px; top: 8px; font-size: 13px; color: var(--lime);
  }
  .search .go {
    position: absolute; right: 6px; top: 6px; width: 30px; height: 18px;
    border-radius: 9px; background: var(--lime); border: 2px solid #e7eaa6;
  }
  .hero {
    position: absolute; top: 130px; left: 154px; width: 888px; height: 405px;
    background: linear-gradient(100deg, #2a2f31 0%, #5b6163 30%, #9a9fa1 55%, #b9bdbe 75%, #6f7576 100%);
  }
  .about {
    position: absolute; top: 535px; left: 154px; width: 888px; height: 276px;
    background: var(--panel); padding: 14px 16px 0 15px;
  }
  .about h1 { font-size: 20px; font-weight: 700; color: var(--lime); margin-bottom: 21px; }
  .about p { font-size: 14px; line-height: 17px; color: var(--ink); }
  .social {
    position: absolute; right: 16px; bottom: 6px;
    display: flex; gap: 14px; align-items: center; font-size: 14px;
  }
  .social a { color: var(--ink); text-decoration: none; font-weight: 700; }
  .footer-band {
    position: absolute; top: 811px; left: 0; width: 1200px; height: 9px;
    background: var(--footer);
  }
</style>
</head>
<body>
  <header class="brand">
    <span class="brand-mark"></span>
    <span class="brand-name">LARKIN ELECTRICAL</span>
  </header>

  <nav class="main-nav">
    <a class="active" href="#" style="left:157px">About Us</a>
    <a href="#" style="left:267px">Our Services</a>
    <a href="#" style="left:405px">Gallery</a>
    <a href="#" style="left:500px">Contact Us</a>
    <a href="#" style="left:624px">Connect with us</a>
    <div class="search">
      <svg class="lens" width="16" height="16" viewBox="0 0 16 16">
        <circle cx="6.5" cy="6.5" r="4.5" fill="none" stroke="#555" stroke-width="2"/>
        <line x1="10" y1="10" x2="14" y2="14" stroke="#555" stroke-width="2.5" stroke-linecap="round"/>
      </svg>
      <span class="divider"></span>
      <span class="placeholder">search</span>
      <span class="go"></span>
    </div>
  </nav>

  <div class="hero" role="img" aria-label="Interior photo of a modern open-plan living space with grey walls, colourful sofa, white chairs and a white dining table"></div>

  <section class="about">
    <h1>A word about Larkin</h1>
    <p>Welcome to Larkin Electrical, my name is Sam Harlow and I’m the director of this exciting electrical business, I’d love the opportunity to share my story with you,<br>
    Throughout my time as an apprentice I had a passion for the latest technology and a strong desire to one day be able to offer the greatest advice, I gained valuable insight working with experienced tradesman and businessman, All of whom both mentored and challenged me in different ways, though something was missing, it wasn’t always smooth sailing and certain challenges arose, whilst service was rarely a priority, but what could I, a mere apprentice do to change things…?<br>
    Well within every challenge lies a fantastic opportunity! I was frustratedby the thought of being stuck in an aging workforce and in an industry built on oldfundamentals for a moment longer, I decided it was time, Time to take control of the situation and create a company built on solid foundations, new ideas and strong ethics!<br>
    Well, Thanks for taking the time to check us out, I hope to work with you in the not too distant future,<br>
    Kindest regards,</p>
    <div class="social">
      <a href="#">palsphere</a>
      <a href="#">chirpnet</a>
      <a href="#" aria-label="Email">
        <svg width="20" height="14" viewBox="0 0 20 14">
          <rect x="1" y="1" width="18" height="12" fill="none" stroke="#0f3338" stroke-width="2"/>
          <polyline points="1,1 10,8 19,1" fill="none" stroke="#0f3338" stroke-width="2"/>
        </svg>
      </a>
    </div>
  </section>

  <div class="footer-band"></div>
</body>
</html>
```